Personal creative Biz Card Design

Need personal yet natural and organic design. The cards I have now are well designed but look too commercial. I want more organic FEELING kind of card. I thought having a headshot would make it more personal... but maybe a sketch effect (or line drawing effect) of face better (?). Maybe in a gray or tungsten color?

Target Market(s)

Well, everyone i give card to will have already seen me face-to-face so that is one thing. Mostly yoga students and people interested in improving their fitness or general health. People looking for wellness, a personal fitness trainer, a yoga teacher

Industry/Entity Type

Health And Wellness

Contact Information for Business Card

I provided examples

Requirements
Must have
• My main logo
• My name

```html
<!DOCTYPE html>
<html lang="en">
<head>
<meta charset="utf-8">
<title>Rowan Tellis – Business Card</title>
<link rel="stylesheet" href="https://fonts.googleapis.com/css2?family=Montserrat:wght@600;700&family=Questrial&display=swap">
<style>
  :root {
    --backdrop: #1c1c1c;
    --card-white: #ffffff;
    --lime: #8fc641;
    --lime-light: #a6d45a;
    --green: #3f9a3c;
    --green-deep: #0b6b35;
    --stripe-gray: #3f3f3f;
    --ink: #2b2b2b;
    --logo-ink-back: #4d7a2a;
  }
  html, body {
    margin: 0;
    padding: 0;
    width: 1200px;
    height: 896px;
    overflow: hidden;
    background: var(--backdrop);
  }
  .canvas {
    position: relative;
    width: 1200px;
    height: 896px;
  }
  .card {
    position: absolute;
    width: 600px;
    height: 343px;
    border-radius: 22px;
    overflow: hidden;
  }
  .card--back {
    left: 520px;
    top: 70px;
    background: linear-gradient(120deg, var(--lime) 0%, var(--lime) 45%, var(--lime-light) 55%, var(--lime) 68%);
  }
  .brand {
    position: absolute;
    display: flex;
    align-items: center;
    gap: 12px;
    font-family: "Montserrat", sans-serif;
    font-weight: 700;
    letter-spacing: 0.5px;
  }
  .brand__dot {
    border-radius: 50%;
    flex: none;
  }
  .card--back .brand {
    left: 140px;
    top: 146px;
    font-size: 40px;
    color: var(--logo-ink-back);
  }
  .card--back .brand__dot {
    width: 34px;
    height: 34px;
    background: var(--logo-ink-back);
  }
  .card--front {
    left: 80px;
    top: 450px;
    background: var(--card-white);
  }
  .wave {
    position: absolute;
    left: 0;
    top: 0;
    width: 600px;
    height: 343px;
  }
  .contact {
    position: absolute;
    left: 40px;
    top: 26px;
    font-family: "Questrial", sans-serif;
    color: var(--ink);
  }
  .contact__name {
    margin: 0;
    font-family: "Montserrat", sans-serif;
    font-weight: 700;
    font-size: 21px;
    line-height: 1.2;
    color: var(--green);
  }
  .contact__title {
    margin: 0 0 16px;
    font-size: 16px;
    line-height: 1.2;
  }
  .contact__address {
    margin: 0 0 6px;
    font-size: 16px;
    line-height: 1.3;
    font-style: normal;
  }
  .contact__list {
    list-style: none;
    margin: 0;
    padding: 0;
    font-size: 16px;
    line-height: 1.35;
  }
  .contact__list li {
    display: flex;
    align-items: center;
    gap: 10px;
  }
  .icon {
    width: 12px;
    height: 12px;
    flex: none;
    fill: var(--green);
  }
  .card--front .brand {
    right: 40px;
    top: 118px;
    font-size: 28px;
    color: var(--green);
  }
  .card--front .brand__dot {
    width: 24px;
    height: 24px;
    background: var(--green);
  }
</style>
</head>
<body>
<main class="canvas">
  <section class="card card--back" aria-label="Card back">
    <div class="brand"><span class="brand__dot"></span>Rowan Tellis</div>
  </section>

  <section class="card card--front" aria-label="Card front">
    <svg class="wave" viewBox="0 0 600 343" aria-hidden="true">
      <defs>
        <linearGradient id="waveFill" x1="0" y1="0" x2="1" y2="0">
          <stop offset="0" stop-color="#0b6b35"/>
          <stop offset="0.5" stop-color="#5aa77e"/>
          <stop offset="0.7" stop-color="#1f7f45"/>
          <stop offset="1" stop-color="#0b6b35"/>
        </linearGradient>
      </defs>
      <path d="M0,252 C60,290 150,300 240,298 C340,296 470,290 600,316 L600,324 C470,298 340,306 240,308 C150,310 60,302 0,264 Z" fill="#3f3f3f"/>
      <path d="M0,270 C70,304 160,314 260,311 C370,308 480,304 600,330 L600,343 L0,343 Z" fill="#8fc641"/>
      <path d="M0,278 C70,312 160,321 260,318 C370,315 480,312 600,336 L600,343 L0,343 Z" fill="#4aa446"/>
      <path d="M0,284 C70,318 160,327 260,324 C370,321 480,318 600,341 L600,343 L0,343 Z" fill="url(#waveFill)"/>
    </svg>

    <div class="contact">
      <h1 class="contact__name">Your Name</h1>
      <p class="contact__title">Job Title</p>
      <address class="contact__address">PO Box No. 123, Street Name<br>City Name, Country 4567</address>
      <ul class="contact__list">
        <li><svg class="icon" viewBox="0 0 12 12"><path d="M1 4 Q6 0 11 4 L9 6 L8 4 L4 4 L3 6 Z M3 7 H9 V11 H3 Z"/></svg>(123) 456 7890</li>
        <li><svg class="icon" viewBox="0 0 12 12"><rect x="3" y="0.5" width="6" height="11" rx="1" fill="none" stroke="#3f9a3c" stroke-width="1.2"/></svg>(123) 456 7890</li>
        <li><svg class="icon" viewBox="0 0 12 12"><path d="M0 2 H12 V10 H0 Z M0 2 L6 7 L12 2" fill="#3f9a3c" stroke="#fff" stroke-width="0.8"/></svg>info@rowantellis.com</li>
        <li><svg class="icon" viewBox="0 0 12 12"><circle cx="6" cy="6" r="5.5"/><path d="M0.5 6 H11.5 M6 0.5 V11.5" stroke="#fff" stroke-width="0.8"/></svg>www.rowantellis.com</li>
      </ul>
    </div>

    <div class="brand"><span class="brand__dot"></span>Rowan Tellis</div>
  </section>
</main>
</body>
</html>
```